Structural Engineering Business Card

Orvik Drafting does residential house plans for clients in Central Florida. Would like simple but elegant business card that is appropriate for a house plan engineering company. Prefer black business card with black/white them but open to other shades of blue. I uploaded a sample card that I came across that looked good but please come up with your own creative designs.

Contact Information for Business Card

Name, Title, Phone, Email, Address, website

```html
<!DOCTYPE html>
<html lang="en">
<head>
<meta charset="utf-8">
<title>Orvik Drafting — Business Card</title>
<link href="https://fonts.googleapis.com/css2?family=Arimo:wght@400;700&display=swap" rel="stylesheet">
<style>
  :root {
    --ink-navy: #12112b;
    --paper: #ffffff;
    --backdrop: #2a2a2c;
    --text-dark: #111111;
  }
  * { box-sizing: border-box; margin: 0; padding: 0; }
  html, body { width: 1200px; height: 1015px; overflow: hidden; }
  body {
    background: var(--backdrop);
    font-family: "Arimo", Arial, sans-serif;
    position: relative;
  }
  .card {
    position: absolute;
    left: 250px;
    width: 700px;
    height: 400px;
    overflow: hidden;
    box-shadow: 0 12px 30px rgba(0,0,0,0.55);
  }
  .card--front { top: 70px; background: var(--ink-navy); }
  .card--back { top: 545px; background: var(--ink-navy); display: flex; }

  .wordmark {
    display: flex;
    align-items: center;
    gap: 14px;
    font-weight: 700;
    letter-spacing: 2px;
    text-transform: uppercase;
    white-space: nowrap;
  }
  .wordmark__square { display: block; flex: none; }

  .card--front .wordmark {
    position: absolute;
    top: 100px;
    left: 0; right: 0;
    justify-content: center;
    color: var(--paper);
    font-size: 52px;
  }
  .card--front .wordmark__square { width: 40px; height: 40px; background: var(--paper); }

  .url-band {
    position: absolute;
    left: 0; right: 0;
    top: 268px;
    height: 62px;
    background: var(--paper);
    display: flex;
    align-items: center;
    justify-content: center;
    color: var(--text-dark);
    font-size: 17px;
    letter-spacing: 2px;
  }

  .back__brand {
    width: 46%;
    background: var(--paper);
    display: flex;
    align-items: center;
    justify-content: center;
  }
  .back__brand .wordmark { color: var(--text-dark); font-size: 27px; gap: 10px; letter-spacing: 1px; }
  .back__brand .wordmark__square { width: 22px; height: 22px; background: var(--text-dark); }

  .back__details {
    flex: 1;
    color: var(--paper);
    padding: 78px 0 0 42px;
  }
  .person__name { font-weight: 700; font-size: 23px; letter-spacing: 0.5px; }
  .person__title { font-size: 17px; margin-top: 2px; }
  .contact-list { list-style: none; margin-top: 24px; }
  .contact-list li {
    display: flex; align-items: center; gap: 8px;
    font-size: 16px; line-height: 24px;
  }
  .contact-list svg { width: 15px; height: 15px; flex: none; }
  .address { margin-top: 24px; font-size: 16px; line-height: 22px; }
</style>
</head>
<body>

<section class="card card--front">
  <div class="wordmark"><span class="wordmark__square"></span>Orvik Drafting</div>
  <div class="url-band">www.orvikdrafting.com</div>
</section>

<section class="card card--back">
  <div class="back__brand">
    <div class="wordmark"><span class="wordmark__square"></span>Orvik Drafting</div>
  </div>
  <div class="back__details">
    <div class="person__name">MARCUS HALE</div>
    <div class="person__title">Managing Director</div>
    <ul class="contact-list">
      <li>
        <svg viewBox="0 0 16 16" aria-hidden="true"><circle cx="8" cy="8" r="7.2" fill="none" stroke="#fff" stroke-width="1.2"/><path d="M5 4.5l1.6-.3.8 2-1 .8a5 5 0 0 0 2.6 2.6l.8-1 2 .8-.3 1.6c-3.6.3-6.8-2.9-6.5-6.5z" fill="#fff"/></svg>
        407-555 018 264
      </li>
      <li>
        <svg viewBox="0 0 16 16" aria-hidden="true"><rect x="1" y="3.5" width="14" height="9" fill="#fff"/><path d="M1 3.5l7 5 7-5" fill="none" stroke="#12112b" stroke-width="1.2"/></svg>
        hello@orvikdrafting.com
      </li>
      <li>
        <svg viewBox="0 0 16 16" aria-hidden="true"><circle cx="8" cy="8" r="7" fill="#fff"/><g fill="none" stroke="#12112b" stroke-width="0.9"><ellipse cx="8" cy="8" rx="3" ry="7"/><path d="M1 8h14M2.5 4.5h11M2.5 11.5h11"/></g></svg>
        www.orvikdrafting.com
      </li>
    </ul>
    <div class="address">118, Cypress Lane Suite 4<br>32801, Orlando FL</div>
  </div>
</section>

</body>
</html>
```